Packaging for a luxury Hair Straightener
Zielgruppe
We are an Israeli company, that provides high end hair tools (straightener etc.) and hair care (Shampoo etc.). Our target market are women in the age between 20-50 years, that pay extra for higher quality. Our items are rated as high end luxury products. Our main target market is in Israel.
Aufgabenstellung
We are currently looking for a new design for our hair straightener package. We recently worked on our logo and now want to restyle the current packaging with the new logo. The package needs to be simple modern and luxurious, but not as simple as it is now. It needs to have a more professional look with different fonts etc.
Also the current design from where everything is needs to be changed. Like for example what is written on the sides of the box or inside the box to have a catchy phrase instead of the logo. The straightener is also white and has the rose gold logo on it. The slogan of the company is 'give your hair what it deserves'.
The pictures of the current design will be attached. It will be printed on both sides and rose gold hot stamping printing should be in the design but other colors are welcome as well. The box is magnetic box.

```html
<!DOCTYPE html>
<html lang="en">
<head>
<meta charset="utf-8">
<title>Solvane Studio – Hair Straightener Box Lid</title>
<link rel="stylesheet" href="https://fonts.googleapis.com/css2?family=Montserrat:wght@300;400;500&display=swap">
<style>
  :root {
    --page-bg: #f1f1f1;
    --box-white: #ffffff;
    --rose-dark: #a86a7a;
    --rose-light: #e3b5bf;
    --ink: #3a3a3a;
    --ink-soft: #6a6a6a;
    --badge-dark: #1c1c1c;
    --badge-light: #6b6b6b;
    --drawing-tone: #f4f4f4;
    --line-grey: #cfcfcf;
  }
  * { margin: 0; padding: 0; box-sizing: border-box; }
  html, body {
    width: 1200px; height: 953px; overflow: hidden;
    background: var(--page-bg);
    font-family: "Montserrat", sans-serif;
  }
  .box-lid {
    position: absolute; left: 100px; top: 256px;
    width: 1000px; height: 440px;
    background: var(--box-white);
    box-shadow: 0 12px 40px rgba(0,0,0,0.08);
  }
  .rose-stripe {
    position: absolute; left: 58px; top: 0;
    width: 6px; height: 100%;
    background: linear-gradient(180deg, var(--rose-dark), var(--rose-light) 55%, var(--rose-dark));
  }
  .cert-badge {
    position: absolute; right: 58px; top: 22px;
    width: 92px; height: 92px; border-radius: 6px;
    background: linear-gradient(160deg, var(--badge-light), var(--badge-dark) 60%);
  }
  .product-drawing {
    position: absolute; left: 150px; top: 140px;
    width: 800px; height: 150px; border-radius: 8px;
    background: linear-gradient(90deg, var(--drawing-tone), #fbfbfb);
    border: 1px solid #ececec;
  }
  .model-line {
    position: absolute; left: 110px; top: 350px;
    display: flex; align-items: center; gap: 14px;
  }
  .model-tag {
    width: 42px; height: 42px;
    border: 1px solid var(--ink-soft); border-radius: 5px;
    display: flex; align-items: center; justify-content: center;
    font-weight: 300; font-size: 20px; color: var(--ink);
  }
  .model-desc {
    font-size: 9px; letter-spacing: 2px; color: var(--ink-soft);
    text-transform: uppercase;
  }
  .brand {
    position: absolute; left: 0; right: 0; top: 330px;
    text-align: center;
  }
  .brand-name {
    font-weight: 400; font-size: 22px; letter-spacing: 4px;
    color: var(--rose-dark); text-transform: uppercase;
  }
  .slogan {
    margin-top: 22px;
    font-size: 8px; letter-spacing: 2.5px; color: var(--ink-soft);
    text-transform: uppercase;
  }
</style>
</head>
<body>
  <main class="box-lid">
    <div class="rose-stripe"></div>
    <div class="cert-badge" aria-hidden="true"></div>
    <div class="product-drawing" role="img" aria-label="Line drawing of the white hair straightener with open plates and cable"></div>
    <div class="model-line">
      <div class="model-tag">V5</div>
      <p class="model-desc">Professional Hair Straightener</p>
    </div>
    <div class="brand">
      <p class="brand-name">Solvane Studio</p>
      <p class="slogan">Give your hair what it deserves</p>
    </div>
  </main>
</body>
</html>
```